Business card design needed

We do excavation, cartage and contracting
I would quote like to have a picture of my digger as the whole back ground and the words on top. If that looks any good
Otherwise please feel free to come up with any other cool options

Cheers Marc

KLR Contracting
Excavation, Cartage, Contracting
Marcus Prewitt
www.klr-example.co.nz
021 584 067
marc@klr-example.co.nz

```html
<!DOCTYPE html>
<html lang="en">
<head>
<meta charset="utf-8">
<title>KLR Contracting – Business Card</title>
<link rel="stylesheet" href="https://fonts.googleapis.com/css2?family=Noto+Sans:wght@400;700&display=swap">
<style>
  :root {
    --card-bg: #ffffff;
    --ink: #000000;
    --brand-green: #1f4f24;
    --card-border: #000000;
  }
  html, body {
    margin: 0;
    padding: 0;
    width: 1200px;
    height: 694px;
    overflow: hidden;
    background: var(--card-bg);
  }
  .card {
    position: relative;
    box-sizing: border-box;
    width: 1200px;
    height: 694px;
    border: 1px solid var(--card-border);
    background: var(--card-bg);
    font-family: "Noto Sans", Tahoma, sans-serif;
    color: var(--ink);
  }
  .line {
    position: absolute;
    left: 0;
    right: 0;
    margin: 0;
    text-align: center;
    white-space: nowrap;
    line-height: 1;
  }
  .brand-mark {
    top: 118px;
    font-weight: 700;
    font-size: 118px;
    letter-spacing: 2px;
    color: var(--brand-green);
  }
  .company-name {
    top: 290px;
    padding-left: 26px;
    font-weight: 700;
    font-size: 52px;
  }
  .services {
    top: 351px;
    padding-left: 26px;
    font-weight: 400;
    font-size: 30px;
  }
  .person-name {
    top: 440px;
    padding-left: 36px;
    font-weight: 700;
    font-size: 42px;
  }
  .phone {
    top: 539px;
    padding-left: 14px;
    font-weight: 400;
    font-size: 31px;
  }
  .web-contacts {
    top: 584px;
    font-weight: 400;
    font-size: 31px;
  }
  .web-contacts .email {
    margin-right: 44px;
  }
</style>
</head>
<body>
  <main class="card">
    <p class="line brand-mark">KLR</p>
    <h1 class="line company-name">KLR Contracting</h1>
    <p class="line services">Excavation, Cartage, Contracting</p>
    <h2 class="line person-name">Marcus Prewitt</h2>
    <p class="line phone">021 584 067</p>
    <p class="line web-contacts"><span class="email">marc@klr-example.co.nz</span><span class="website">www.klr-example.co.nz</span></p>
  </main>
</body>
</html>
```